Used Car Business Card Design

Maple Ridge Auto Sales is a woman owned women friendly car lot.  We focus on providing Professionalism, Integrity and Respect beginning with the initial introduction.  We place the highest importance on customer service after the sale and our rating with the TVB of Arkansas shows it.  We're starting out 7th year, recently relocated. Satisfied Clients bring their family members, friends and co-workers to buy their cars, SUV's and trucks from MRAS.
You buy here / you pay here, Lending program opportunities too, Great Cash Prices
Finance with Flexibility we look at each individual uniquely and not a credit score
I think of my kids when getting our vehicles ready and your safety when you drive away in a MRAS car. . .  Drive away with Peace of Mind...
Maroon, Black and Silver colors.

Updates
I sent a response to the designers - have  not heard from them, will I receive my funds back?

Thank you all,  a lot of great designs - Making my decision on Nov 4th

So much talent. . .
So very challenging. . .
Thank you for your participation.
Sincerely,
Maple Ridge Auto Sales
Lorna Pickett

Industry/Entity Type
Safety
Contact Information for Business Card
Maple Ridge Auto Sales
"A Sound Car for a Fair Price"
4153 Garvey Rd. East Harlow Springs, Ms 38990
Lorna Pickett
501.389.7312

```html
<!DOCTYPE html>
<html lang="en">
<head>
<meta charset="utf-8">
<title>Maple Ridge Auto Sales – Business Card</title>
<link rel="stylesheet" href="https://fonts.googleapis.com/css2?family=Open+Sans:wght@300;400;700&display=swap">
<style>
  :root {
    --maroon: #9a1a1f;
    --maroon-deep: #7e1418;
    --maroon-light: #a8242a;
    --charcoal: #4a4a4c;
    --silver: #b9b9bb;
    --paper: #ffffff;
    --paper-shade: #eeeeee;
    --backdrop: #e6e4e1;
  }
  * { margin: 0; padding: 0; box-sizing: border-box; }
  html, body { width: 1200px; height: 1000px; overflow: hidden; }
  body {
    background: var(--backdrop);
    font-family: "Open Sans", Arial, sans-serif;
    position: relative;
  }
  .card {
    position: absolute;
    top: 346px;
    width: 540px;
    height: 309px;
    overflow: hidden;
    box-shadow: 0 6px 18px rgba(0,0,0,0.18);
  }
  .card--front { left: 40px; background: linear-gradient(160deg, var(--paper) 40%, var(--paper-shade) 100%); }
  .card--back { left: 620px; }
  .card svg { position: absolute; inset: 0; }

  .brand { position: absolute; color: var(--maroon); font-weight: 300; line-height: 1; }
  .brand__name { display: block; font-size: 30px; letter-spacing: -0.5px; }
  .brand__sub { display: block; font-size: 10px; letter-spacing: 6px; margin-top: 4px; padding-left: 60px; }
  .card--front .brand { left: 26px; top: 184px; }

  .divider { position: absolute; left: 214px; top: 176px; width: 1px; height: 92px; background: var(--silver); }

  .contact { position: absolute; left: 230px; top: 188px; color: var(--charcoal); font-size: 11.5px; line-height: 19px; }
  .contact__name { font-size: 17px; font-weight: 700; line-height: 22px; margin-bottom: 2px; }

  .card--back .brand { color: var(--paper); left: 0; right: 0; top: 112px; text-align: center; }
  .card--back .brand__name { font-size: 34px; }
  .card--back .brand__sub { padding-left: 90px; }
  .tagline {
    position: absolute; left: 0; right: 0; top: 190px;
    text-align: center; color: var(--paper); font-size: 13px; font-weight: 300; letter-spacing: 0.5px;
  }
</style>
</head>
<body>

  <section class="card card--front" aria-label="Business card front">
    <svg width="540" height="309" viewBox="0 0 540 309">
      <defs>
        <linearGradient id="facetFront" x1="0" y1="0" x2="1" y2="1">
          <stop offset="0" stop-color="#8a171b"/>
          <stop offset="0.5" stop-color="#a3212a"/>
          <stop offset="1" stop-color="#861519"/>
        </linearGradient>
      </defs>
      <path role="img" aria-label="Maroon faceted low-poly band"
            d="M210,0 L540,0 L540,309 L470,309 L400,205 L335,178 L275,70 L235,52 Z"
            fill="url(#facetFront)"/>
    </svg>
    <div class="brand">
      <span class="brand__name">Maple Ridge</span>
      <span class="brand__sub">AUTO SALES</span>
    </div>
    <div class="divider"></div>
    <div class="contact">
      <p class="contact__name">Lorna Pickett</p>
      <p>501.389.7312</p>
      <p>4153 Garvey Rd. East</p>
      <p>Harlow Springs, Ms 38990</p>
    </div>
  </section>

  <section class="card card--back" aria-label="Business card back">
    <svg width="540" height="309" viewBox="0 0 540 309">
      <defs>
        <radialGradient id="facetBack" cx="0.5" cy="0.45" r="0.75">
          <stop offset="0" stop-color="#a8242a"/>
          <stop offset="0.6" stop-color="#961b20"/>
          <stop offset="1" stop-color="#7e1418"/>
        </radialGradient>
      </defs>
      <rect role="img" aria-label="Maroon faceted low-poly background"
            width="540" height="309" fill="url(#facetBack)"/>
    </svg>
    <div class="brand">
      <span class="brand__name">Maple Ridge</span>
      <span class="brand__sub">AUTO SALES</span>
    </div>
    <p class="tagline">A Sound Car for a Fair Price</p>
  </section>

</body>
</html>
```